Slate App design for business management system

TaskOra is a business management system made especially for service based businesses (our subscribers). It enables systemising your service businesses. This can be used by diverse industries like automotive service, beauty (hair salons, nail spas), Spas, Chiropractor, acupuntcure, osteo, yoga studio, business coach, etc.

The UI of the app needs to be designed using flat and clean UI design trends that are currently prevailing for B2C apps. Even the sliding menu panel can be removed and alternative placement of this functionality can be suggested. The color palette used for the design should be limited (3-5 colours)

The Current UI screens are open to suggestions for change. For ease of management in minimum steps, consolidation of functionality on different screens can be suggested, accompanies by a rational reason with the objective of having a simple and straight forward user experience.

User should be able to move from one function to another (booking > view appointments > profile) in no more than 1 or max 2 gestures.

Target Market(s)

SME businesses that provide time based services

Industry/Entity Type

Business

Font styles to use
Sans Serif

Requirements
Must have
• The power point slides give a detailed account of the process flow and functionality that the app is to follow.
• Reference this slide to ensure that your final design must have all screens that are required to deliver the functionality.

```html
<!DOCTYPE html>
<html lang="en">
<head>
<meta charset="utf-8">
<title>TaskOra – Log In</title>
<link rel="stylesheet" href="https://fonts.googleapis.com/css2?family=Roboto:wght@400;500&family=Great+Vibes&display=swap">
<style>
  :root {
    --ink: #4a4a4a;
    --muted: #7a7a7a;
    --field-bg: rgba(248, 246, 243, 0.88);
    --field-border: rgba(255, 255, 255, 0.7);
    --divider: #c9c6c2;
    --brand-brown: #55341a;
    --white: #ffffff;
    --link: #f1ece6;
  }
  * { box-sizing: border-box; margin: 0; padding: 0; }
  html, body { width: 1200px; height: 900px; overflow: hidden; }
  body { font-family: "Roboto", Arial, sans-serif; position: relative; background: #6d7a84; }

  .backdrop {
    position: absolute; inset: 0;
    background:
      radial-gradient(ellipse 420px 260px at 90px 400px, rgba(250,250,240,0.95), rgba(250,250,240,0) 70%),
      radial-gradient(ellipse 520px 200px at 620px 560px, rgba(225,200,180,0.85), rgba(225,200,180,0) 70%),
      radial-gradient(ellipse 380px 300px at 200px 820px, rgba(40,32,18,0.9), rgba(40,32,18,0) 70%),
      radial-gradient(ellipse 340px 220px at 1130px 880px, rgba(120,90,50,0.8), rgba(120,90,50,0) 70%),
      linear-gradient(180deg, rgba(0,0,0,0) 0%, rgba(0,0,0,0) 55%, rgba(45,50,48,0.85) 75%, rgba(55,45,28,0.95) 100%),
      linear-gradient(115deg, #e9ecee 0%, #c7d0da 30%, #8fa4bd 55%, #557898 80%, #4b6e92 100%);
  }

  .status-bar {
    position: absolute; top: 0; left: 0; right: 0; height: 40px;
    display: flex; align-items: center; justify-content: space-between;
    padding: 0 18px; color: #222; font-size: 16px;
  }
  .status-bar .left, .status-bar .right { display: flex; align-items: center; gap: 7px; }
  .status-bar .time { position: absolute; left: 50%; transform: translateX(-50%); font-weight: 500; }
  .status-bar .right { color: #eef2f6; }

  .welcome {
    position: absolute; top: 140px; left: 0; right: 0; text-align: center;
    font-family: "Great Vibes", cursive; font-size: 92px; color: var(--ink); line-height: 1;
  }

  .login-form { position: absolute; left: 272px; top: 339px; width: 655px; }
  .field {
    height: 69px; display: flex; align-items: center;
    background: var(--field-bg); border: 1px solid var(--field-border);
    margin-bottom: 19px;
  }
  .field .icon { width: 76px; display: flex; justify-content: center; }
  .field .sep { width: 1px; height: 42px; background: var(--divider); }
  .field .placeholder { margin-left: 21px; font-size: 17.5px; color: var(--muted); }

  .btn-login {
    margin-top: 80px; height: 68px; background: var(--brand-brown);
    display: flex; align-items: center; justify-content: center; gap: 16px;
    color: var(--white); font-size: 21px; font-weight: 500; letter-spacing: 0.3px;
  }
  .links {
    margin-top: 16px; display: flex; justify-content: center; align-items: center;
    font-size: 16px; color: var(--link);
  }
  .links a { color: var(--link); text-decoration: underline; text-underline-offset: 3px; }
  .links .bar { width: 1px; height: 21px; background: #2c2c2c; margin: 0 54px 0 46px; }
</style>
</head>
<body>
  <div class="backdrop" role="img" aria-label="Softly blurred landscape at dusk, pale sky fading to dark ground"></div>

  <header class="status-bar">
    <div class="left">
      <span>Slate</span>
      <svg width="18" height="14" viewBox="0 0 18 14"><path d="M1 5a11 11 0 0 1 16 0M4 8a7 7 0 0 1 10 0M7 11a3 3 0 0 1 4 0" fill="none" stroke="#222" stroke-width="2" stroke-linecap="round"/></svg>
    </div>
    <span class="time">4:21 PM</span>
    <div class="right">
      <svg width="10" height="16" viewBox="0 0 10 16"><path d="M1 4l8 8-4 3V1l4 3-8 8" fill="none" stroke="#dfe5ec" stroke-width="1.2"/></svg>
      <span>100%</span>
      <svg width="38" height="16" viewBox="0 0 38 16"><rect x="1" y="2" width="33" height="12" rx="2.5" fill="none" stroke="#111" stroke-width="1"/><rect x="3" y="4" width="29" height="8" rx="1" fill="#111"/><rect x="35" y="6" width="2" height="4" fill="#111"/></svg>
    </div>
  </header>

  <h1 class="welcome">Welcome</h1>

  <form class="login-form">
    <div class="field">
      <span class="icon">
        <svg width="38" height="38" viewBox="0 0 38 38"><circle cx="19" cy="12" r="8" fill="none" stroke="#8a8a8a" stroke-width="1.8"/><path d="M3 36c0-9 7-14 16-14s16 5 16 14z" fill="none" stroke="#8a8a8a" stroke-width="1.8" stroke-linejoin="round"/></svg>
      </span>
      <span class="sep"></span>
      <span class="placeholder">User Name</span>
    </div>
    <div class="field">
      <span class="icon">
        <svg width="30" height="38" viewBox="0 0 30 38"><path d="M6 16v-5a9 9 0 0 1 18 0v5" fill="none" stroke="#999" stroke-width="2"/><rect x="2" y="15" width="26" height="21" rx="3" fill="#999"/></svg>
      </span>
      <span class="sep"></span>
      <span class="placeholder">Password</span>
    </div>

    <div class="btn-login">
      <svg width="24" height="20" viewBox="0 0 24 20"><path d="M8 1h15v18H8M1 10h14M11 6l4 4-4 4" fill="none" stroke="#fff" stroke-width="1.3"/></svg>
      <span>LOG IN</span>
    </div>

    <nav class="links">
      <a href="#">Forgot Password?</a>
      <span class="bar"></span>
      <a href="#">Need Accound</a>
    </nav>
  </form>
</body>
</html>
```